Job Coaching - Falo; engaging people to improve their work experience

design a website focussed on people
with 4 tabs/pages (+2)
1) landing page
2) Professional
3) Job Coaching
4) Bio
5) Contact
6) references

I've added the text to be used in the documents. The website will be in Dutch, but I've added the translations in green just for you to understand what it is about.

I've added my logo as well, and a flyer I used already. this gives you an idea on how it could look like
Pictures you can find there as well. Other pictures can be added of course
The techical creation of the website is not needed. I need all the designs and information to be able to create it myself.

```html
<!DOCTYPE html>
<html lang="nl">
<head>
<meta charset="utf-8">
<title>Falo – Loopbaancheque</title>
<link href="https://fonts.googleapis.com/css2?family=Poppins:wght@400;500;600;700;800&display=swap" rel="stylesheet">
<style>
  :root {
    --teal: #35a99c;
    --teal-dark: #2a9589;
    --ink: #232323;
    --white: #ffffff;
    --footer: #151515;
    --hero-a: #1aa9cc;
    --hero-b: #0f6f8e;
    --wood: #8a6a55;
  }
  * { margin: 0; padding: 0; box-sizing: border-box; }
  html, body { width: 768px; height: 1200px; overflow: hidden; }
  body { font-family: "Poppins", sans-serif; color: var(--ink); background: var(--white); position: relative; }

  .site-header { position: absolute; top: 0; left: 0; width: 768px; height: 53px; border-top: 2px solid var(--teal); background: var(--white); }
  .brand { position: absolute; display: flex; align-items: center; gap: 6px; font-weight: 600; color: var(--teal); }
  .brand-dot { width: 20px; height: 20px; border-radius: 50%; background: var(--teal); }
  .site-header .brand { left: 71px; top: 11px; font-size: 24px; line-height: 28px; }
  .main-nav { position: absolute; top: 21px; left: 0; font-size: 10px; }
  .main-nav a { position: absolute; white-space: nowrap; color: var(--ink); text-decoration: none; }
  .main-nav a.active { color: var(--teal); }
  .main-nav a.active::after { content: ""; position: absolute; left: 0; right: 0; top: 27px; height: 3px; border-radius: 3px 3px 0 0; background: var(--teal); }
  .btn-contact { position: absolute; left: 619px; top: 14px; width: 78px; height: 27px; border-radius: 14px; background: var(--teal); color: var(--white); font-size: 8.5px; font-weight: 600; display: flex; align-items: center; justify-content: center; gap: 8px; letter-spacing: .3px; }

  .hero { position: absolute; top: 53px; left: 0; width: 768px; height: 378px; overflow: hidden;
    background: radial-gradient(ellipse at 45% 35%, var(--hero-a) 0%, #1593b5 50%, var(--hero-b) 100%); }
  .hero-floor { position: absolute; left: 0; bottom: 0; width: 100%; height: 42px; background: linear-gradient(#5a4a40, var(--wood)); }
  .hero-title { position: absolute; top: 136px; width: 100%; text-align: center; color: var(--white); font-weight: 700; font-size: 35px; letter-spacing: .5px; }
  .hero-sub { position: absolute; top: 180px; width: 100%; text-align: center; color: var(--white); font-weight: 500; font-size: 16px; }

  .intro-photo-frame { position: absolute; left: 59px; top: 630px; width: 87px; height: 83px; border-radius: 8px; background: var(--teal); }
  .intro-photo { position: absolute; left: 71px; top: 485px; width: 287px; height: 216px; border-radius: 8px; background: linear-gradient(135deg, #6f7a70 0%, #9a8b78 50%, #7a2a33 100%); }

  .bullets { position: absolute; list-style: none; font-size: 11px; line-height: 17.2px; text-align: justify; }
  .bullets li { position: relative; padding-left: 13px; }
  .bullets li::before { content: ""; position: absolute; left: 0; top: 6px; width: 5px; height: 5px; border-radius: 50%; background: var(--teal); }
  .bullets em { font-style: normal; color: var(--teal); font-weight: 500; }
  .bullets-side { left: 375px; top: 489px; width: 322px; }
  .bullets-side li + li { margin-top: 14px; }
  .bullets-wide { left: 71px; top: 732px; width: 626px; }

  .cta-band { position: absolute; top: 835px; left: 0; width: 768px; height: 179px; background: linear-gradient(90deg, #3aa79a, var(--teal) 50%, #33a598); color: var(--white); text-align: center; }
  .cta-title { position: absolute; top: 33px; width: 100%; font-size: 33px; font-weight: 700; line-height: 40px; }
  .cta-sub { position: absolute; top: 73px; width: 100%; font-size: 20px; line-height: 26px; }
  .cta-text { position: absolute; top: 108px; left: 184px; width: 400px; font-size: 11px; line-height: 17.5px; }

  .site-footer { position: absolute; top: 1014px; left: 0; width: 768px; height: 186px; background: var(--footer); color: var(--white); }
  .site-footer .brand { left: 0; right: 0; justify-content: center; top: 44px; font-size: 28px; line-height: 32px; }
  .site-footer .brand-dot { width: 24px; height: 24px; }
  .footer-nav { position: absolute; top: 116px; left: 0; width: 100%; display: flex; justify-content: center; gap: 26px; font-size: 10px; font-weight: 500; }
  .footer-rule { position: absolute; top: 146px; left: 71px; width: 626px; height: 1px; background: #1f3a36; }
  .copyright { position: absolute; top: 161px; width: 100%; text-align: center; font-size: 8.5px; font-weight: 500; }
</style>
</head>
<body>
  <header class="site-header">
    <div class="brand"><span class="brand-dot"></span>Falo</div>
    <nav class="main-nav">
      <a class="active" style="left:271px">Thuis</a>
      <a style="left:322px">Professioneel</a>
      <a style="left:413px">Job Coaching</a>
      <a style="left:505px">Bio</a>
      <a style="left:545px">Referenties</a>
    </nav>
    <div class="btn-contact">CONTACT
      <svg width="6" height="8" viewBox="0 0 6 8"><path d="M1 1l3 3-3 3" fill="none" stroke="#fff" stroke-width="1.3"/></svg>
    </div>
  </header>

  <section class="hero">
    <div role="img" aria-label="Houten figuur die houten traptreden opstapt, een hand plaatst de volgende tree" style="position:absolute;inset:0"></div>
    <div class="hero-floor"></div>
    <h1 class="hero-title">LOOPBAANCHEQUE</h1>
    <p class="hero-sub">Verkrugbaar via</p>
  </section>

  <div class="intro-photo-frame"></div>
  <div class="intro-photo" role="img" aria-label="Portret van loopbaancoach Tom Verhaegen"></div>

  <ul class="bullets bullets-side">
    <li>Hallo, ik ben Tom Verhaegen. <em>Als gepassioneerd loopbaancoach</em> wil ik jou in je kracht zetten bij het uitoefenen van je job, elke dag opnieuw.</li>
    <li>We blijven steeds langer aan <em>de slag en daarom is het vandaag meer dan ooit</em> belangrijk om de nodige aandacht te besteden aan professionele groei en welzijn op het werk.</li>
    <li>Ik ben ervan overtuigd dat <em>mensen vaak tot meer</em> in staat zijn dan ze zelf geloven. Alles begint met het verlangen naar verandering. Wie ben ik? Wat is mijn rol? Wat wil ik écht?</li>
  </ul>

  <ul class="bullets bullets-wide">
    <li>Als jobcoach ga ik niet voor <em>eenvoudige quick-wins of kant-en-klare</em> tips en tricks. In een geest van openheid, vertrouwen en gelijkwaardigheid gaan we samen op zoek naar de <em>diepere inzichten en duurzame oplossingen</em> die voor jou werken. Coaching is een bewustwordingsproces dat leidt tot het vinden van de antwoorden in jezelf.</li>
  </ul>

  <section class="cta-band">
    <h2 class="cta-title">Meld je</h2>
    <p class="cta-sub">vandaag nog</p>
    <p class="cta-text">aan voor een vrijblijvend kennismakingsgesprek en neem de regie van je loopbaan (opnieuw) in handen.</p>
  </section>

  <footer class="site-footer">
    <div class="brand"><span class="brand-dot"></span>Falo</div>
    <nav class="footer-nav">
      <span>Thuis</span><span>Professioneel</span><span>Job Coaching</span><span>Bio</span><span>Referenties</span><span>Contact</span>
    </nav>
    <div class="footer-rule"></div>
    <p class="copyright">©2023. All rights reserved.</p>
  </footer>
</body>
</html>
```